PowerPoint Design Project Oil and Gas Company

For background please visit www.brastonhollowpower.com for our trial web site, attached is a brief write-up on the firm with our logo and styling on our name. Use the colors you see on the web page and write-up

Our audience is technical oil and gas engineers

I need a master slide as well as the five slides completed. Don't spend too much time on the master slide because the design elements, logo and colors have already been chosen so stay with them.

I need it all done by April 8th. I will be chosing quickly and will look to form a long-term relationship for upcoming presentations, collateral sales materials, finishing the web site, etc.

I would appreciate if your first language was English and if you had a technical background or experience with technical issues, preferably oil and gas.

Oil And Gas

```html
<!DOCTYPE html>
<html lang="en">
<head>
<meta charset="utf-8">
<title>Plans – Braston Hollow Power</title>
<link rel="stylesheet" href="https://fonts.googleapis.com/css2?family=Carlito:wght@400;700&family=Gelasio:wght@700&display=swap">
<style>
  :root{
    --page:#eef4e3;
    --title:#8aab4a;
    --rule:#8e8e8e;
    --badge:#9dc83e;
    --head-1:#b9d28f;
    --head-2:#9fc064;
    --head-3:#82ae40;
    --box-1:#bed598;
    --box-2:#a8c874;
    --box-3:#8ab54c;
    --text:#ffffff;
    --band-green-a:#a6d04c;
    --band-green-b:#7fb92e;
    --band-dark:#000000;
  }
  *{margin:0;padding:0;box-sizing:border-box}
  html,body{width:1200px;height:900px;overflow:hidden}
  body{background:var(--page);font-family:"Carlito",Calibri,Arial,sans-serif;position:relative}

  .slide-title{position:absolute;right:32px;top:18px;font-family:"Gelasio",Georgia,serif;font-weight:700;font-size:58px;color:var(--title);letter-spacing:.5px}
  .title-rule{position:absolute;left:125px;top:90px;width:1050px;height:15px;background:var(--rule)}
  .brand-block{position:absolute;left:37px;top:52px;width:94px;height:88px;background:var(--badge);box-shadow:3px 4px 8px rgba(0,0,0,.35)}

  .phase-head{position:absolute;top:179px;height:69px;display:flex;align-items:center;justify-content:center;padding-right:34px;
    clip-path:polygon(0 0,calc(100% - 40px) 0,100% 50%,calc(100% - 40px) 100%,0 100%);
    color:var(--text);font-weight:700;font-size:38px;box-shadow:0 3px 4px rgba(0,0,0,.2)}
  .phase-head--1{left:40px;width:348px;background:linear-gradient(#c6dba1,var(--head-1))}
  .phase-head--2{left:420px;width:348px;background:linear-gradient(#adc975,var(--head-2))}
  .phase-head--3{left:796px;width:367px;background:linear-gradient(#90b94f,var(--head-3))}

  .phase-box{position:absolute;top:266px;border-radius:14px;color:var(--text);font-weight:700}
  .phase-box--1{left:40px;width:350px;height:481px;background:var(--box-1)}
  .phase-box--2{left:419px;width:352px;height:485px;background:var(--box-2);border:2px solid #9dbd66}
  .phase-box--3{left:796px;width:369px;height:481px;background:var(--box-3)}

  .item,.sub{position:absolute;font-size:19px;line-height:24px}
  .item::before{content:"";position:absolute;left:-36px;top:1px;width:22px;height:20px;background:rgba(255,255,255,.55);border:1px solid rgba(255,255,255,.8)}
  .item--1{left:50px}
  .item--2,.item--3{left:51px}
  .sub{left:85px}
  .sub::before{content:"➢";position:absolute;left:-23px;top:0;font-size:17px}
  .sub--wrap{line-height:30px}

  .flow-arrow{position:absolute;top:487px;width:88px;height:69px}
  .flow-arrow--1{left:375px}
  .flow-arrow--2{left:755px}

  .footer-rule{position:absolute;left:0;top:791px;width:1200px;height:18px;background:var(--rule)}
  .footer-green{position:absolute;left:0;top:809px;width:605px;height:91px;background:linear-gradient(var(--band-green-a),var(--band-green-b))}
  .footer-dark{position:absolute;left:605px;top:809px;width:595px;height:91px;background:var(--band-dark);display:flex;align-items:center;justify-content:flex-end;padding-right:40px;gap:16px}
  .footer-mark{width:34px;height:34px;background:#8dbf3c}
  .footer-name{color:#ffffff;font-size:38px;font-weight:400}
</style>
</head>
<body>
  <h1 class="slide-title">Plans</h1>
  <div class="title-rule"></div>
  <div class="brand-block"></div>

  <div class="phase-head phase-head--1">Phase I</div>
  <div class="phase-head phase-head--2">Phase II</div>
  <div class="phase-head phase-head--3">Phase III</div>

  <section class="phase-box phase-box--1">
    <div class="item item--1" style="top:44px">Partnership Structure</div>
    <div class="item item--1" style="top:97px">Business Plan</div>
    <div class="sub" style="top:133px">Market Research Brine</div>
    <div class="sub" style="top:161px">Targets</div>
    <div class="sub" style="top:188px">Go to market plan</div>
    <div class="item item--1" style="top:237px">Engineering</div>
    <div class="sub sub--wrap" style="top:278px">Power/ heat generation-<br>water Treatment balance</div>
    <div class="sub" style="top:343px;line-height:28px">Gas scrubbing for power<br>skids</div>
    <div class="item item--1" style="top:419px">Designer Brine Trial</div>
  </section>

  <section class="phase-box phase-box--2">
    <div class="item item--2" style="top:37px;line-height:29px">Schema ties of systems for<br>multiple sizes</div>
    <div class="item item--2" style="top:117px">Overall system leasing</div>
    <div class="item item--2" style="top:172px">Solution Sale</div>
  </section>

  <section class="phase-box phase-box--3">
    <div class="item item--3" style="top:38px">Marketing roll out</div>
    <div class="item item--3" style="top:88px">Sales implementation</div>
    <div class="item item--3" style="top:143px">Pilot installation</div>
  </section>

  <svg class="flow-arrow flow-arrow--1" viewBox="0 0 88 69" aria-hidden="true"><polygon points="0,17 50,17 50,0 88,34.5 50,69 50,52 0,52" fill="#ffffff"/></svg>
  <svg class="flow-arrow flow-arrow--2" viewBox="0 0 88 69" aria-hidden="true"><polygon points="0,17 50,17 50,0 88,34.5 50,69 50,52 0,52" fill="#ffffff"/></svg>

  <div class="footer-rule"></div>
  <div class="footer-green"></div>
  <div class="footer-dark">
    <span class="footer-mark"></span>
    <span class="footer-name">Braston Hollow Power</span>
  </div>
</body>
</html>
```